Brevimor Inc. Website

We need a website design for a new company based in Montreal, Canada. Our company offers professional services in planning & scheduling for major construction projects in varying industries. The main colors to be used are black & red (same as in logo). The final design should convey professionalism, precision, and excellence. The following are examples of what the website layout could look like: https://www.valqorix.ca/, https://4796.ca/, https://dumelvo.ca/, https://www.quorbintal.com/en. Avoid using stock videos or photos with people in it.
Target Market(s)
Target audience are multi-national clients looking to hire a firm to manage their construction projects. Target market is Mining & Metals
Industry/Entity Type
Mining & Metalurgy, Hydroelectricity, Infrastructure
Number of Pages Required
1 page
Colors
Designer to choose colors to be used in the design.
Look and feel
Each slider illustrates characteristics of the customer's brand and the style your logo design should communicate.

```html
<!DOCTYPE html>
<html lang="en">
<head>
<meta charset="utf-8">
<title>Brevimor Inc. — Planning &amp; Scheduling</title>
<link href="https://fonts.googleapis.com/css2?family=Poppins:wght@400;500;600;700;800&display=swap" rel="stylesheet">
<style>
:root{
  --red:#a50f1c;
  --red-dark:#5c0710;
  --ink:#141414;
  --text:#3a3a3a;
  --muted:#6b6b6b;
  --navy:#17204a;
  --white:#ffffff;
  --line:#c9c9c9;
}
*{box-sizing:border-box;margin:0;padding:0}
html,body{width:1200px;height:5217px;overflow:hidden}
body{font-family:'Poppins',sans-serif;color:var(--text);background:var(--white);position:relative}
.abs{position:absolute}
h1,h2,h3{font-family:'Poppins',sans-serif;color:var(--ink);font-weight:700}
.accent{color:var(--red)}
.btn{position:absolute;display:flex;align-items:center;justify-content:center;background:var(--red);color:var(--white);font-weight:600;border-radius:20px;text-decoration:none}
.circle-btn{position:absolute;border-radius:50%;display:flex;align-items:center;justify-content:center}
.photo{position:absolute}

/* header & hero */
.hero{position:absolute;left:0;top:0;width:1200px;height:700px;overflow:hidden}
.hero-photo{position:absolute;inset:0;background:linear-gradient(180deg,#b9c7e6 0%,#d3d8ea 30%,#c9a987 55%,#7d6a5a 75%,#5a5047 100%)}
.hero-curve{position:absolute;left:0;top:0}
.nav{position:absolute;top:36px;left:195px;display:flex;gap:26px;font-size:11px;color:var(--ink)}
.nav .active{color:var(--red)}
.brand{position:absolute;top:22px;left:500px;width:200px;display:flex;align-items:center;justify-content:center;gap:8px;font-weight:700;font-size:18px;color:var(--red)}
.brand-dot{width:14px;height:14px;border-radius:50%;background:var(--red)}
.careers{position:absolute;top:36px;left:736px;font-size:11px;color:var(--ink)}
.contact{left:821px;top:28px;width:114px;height:35px;font-size:13px}
.lang{position:absolute;top:35px;left:950px;font-size:11px;color:var(--ink);display:flex;align-items:center;gap:4px}
.welcome{position:absolute;top:158px;left:0;width:1200px;text-align:center;font-size:15px;font-weight:500;letter-spacing:2px;color:var(--ink)}
.welcome span{color:var(--red)}
.welcome-dot{position:absolute;left:583px;top:184px;width:34px;height:34px;border-radius:50%;background:var(--ink)}
.hero-title{position:absolute;top:228px;left:0;width:1200px;text-align:center;font-size:39px;line-height:49px;font-weight:700;color:var(--ink)}
.slide-prev{left:95px;top:333px;width:38px;height:38px;background:var(--red)}
.slide-next{left:1080px;top:333px;width:38px;height:38px;border:1.5px solid var(--ink)}
.scroll-down{left:564px;top:669px;width:72px;height:72px;background:var(--red)}

/* who we are */
.who-photo{left:195px;top:843px;width:340px;height:428px;background:linear-gradient(160deg,#3b2d2a,#c96a2a 45%,#f0a24a 60%,#3a2a22)}
.who-photo-2{left:570px;top:1186px;width:413px;height:233px;background:linear-gradient(150deg,#d98a5e,#e7b495 40%,#8fa0ae 70%,#b0705a)}
.who-faint{position:absolute;left:345px;top:1310px;width:222px;text-align:center;font-size:30px;font-weight:700;color:rgba(165,15,28,.14)}
.who-title{position:absolute;left:578px;top:842px;font-size:36px}
.who-lead{position:absolute;left:578px;top:902px;width:410px;padding-left:10px;border-left:2px solid var(--red);color:var(--red);font-size:11.5px;font-weight:500;line-height:19px}
.who-text{position:absolute;left:578px;width:410px;font-size:10px;line-height:18px;color:var(--text)}
.who-btn{left:580px;top:1117px;width:115px;height:35px;font-size:12px}

/* services */
.services{position:absolute;left:0;top:1516px;width:1200px;height:1064px;background:linear-gradient(180deg,#8d0b17 0%,#6d0812 45%,#3a060b 75%,#1c0e10 100%)}
.services-title{position:absolute;top:1593px;left:0;width:1200px;text-align:center;font-size:36px;color:var(--white)}
.svc{position:absolute;width:245px}
.svc-photo{position:absolute;left:0;top:0;width:245px;height:210px}
.svc-box{position:absolute;left:8px;top:210px;width:229px;height:92px;background:var(--white);display:flex;align-items:center;justify-content:center;text-align:center;font-size:15px;font-weight:600;line-height:20px;color:var(--ink);padding-bottom:6px}
.svc-icon{position:absolute;left:81px;top:-41px;width:83px;height:83px;border-radius:50%;background:var(--red);border:3px solid var(--white)}
.svc-arrow{position:absolute;left:106px;top:286px;width:33px;height:33px;border-radius:50%;background:var(--ink);display:flex;align-items:center;justify-content:center}

/* projects */
.projects-title{position:absolute;left:195px;top:2653px;font-size:36px}
.proj{position:absolute;overflow:hidden}
.proj-label{position:absolute;left:20px;bottom:22px;font-size:17px;font-weight:700;color:var(--white);letter-spacing:.3px}

/* build */
.build{position:absolute;left:0;top:3369px;width:1200px;height:375px;background:linear-gradient(180deg,#1a2456,#1c2550 60%,#2b2a3a)}
.build-title{position:absolute;top:3462px;left:0;width:1200px;text-align:center;font-size:36px;line-height:49px;color:var(--white)}
.build-text{position:absolute;top:3570px;left:290px;width:620px;text-align:center;font-size:11px;line-height:20px;color:#e6e6ee}
.build-btn{left:523px;top:3626px;width:154px;height:33px;font-size:11px}

/* news */
.news-title{position:absolute;left:190px;top:3822px;font-size:36px}
.news-prev{left:920px;top:3826px;width:38px;height:38px;border:1.5px solid var(--ink)}
.news-next{left:966px;top:3826px;width:38px;height:38px;background:var(--red)}
.news-card{position:absolute;top:3892px;width:399px;height:476px;background:var(--white);box-shadow:0 6px 18px rgba(0,0,0,.12)}
.news-photo{position:absolute;left:0;top:0;width:399px;height:237px}
.news-body{position:absolute;left:0;top:259px;padding:0 20px;width:399px}
.news-date{font-size:10px;font-weight:600;color:var(--red);border-left:2px solid var(--red);padding-left:18px;margin-left:-20px;line-height:20px}
.news-head{margin-top:20px;font-size:15px;font-weight:500;line-height:23px;color:var(--ink)}
.news-text{margin-top:14px;font-size:10px;line-height:18px;color:var(--text)}
.news-link{display:inline-block;margin-top:16px;font-size:12px;font-weight:600;color:var(--red);text-decoration:underline}

/* footer */
.footer{position:absolute;left:0;top:4480px;width:1200px;height:737px;background:linear-gradient(180deg,#ffffff 0%,#dfe9f2 20%,#d4e2ee 60%,#c8d4de 100%)}
.footer-brand{position:absolute;top:4585px;left:0;width:1200px;display:flex;justify-content:center;align-items:center;gap:10px;font-size:26px;font-weight:700;color:var(--red)}
.footer-brand .brand-dot{width:22px;height:22px}
.social{position:absolute;top:4699px;width:36px;height:36px;border-radius:50%;background:var(--ink)}
.footer-rule{position:absolute;left:195px;width:810px;height:1px;background:var(--line)}
.footer-nav{position:absolute;top:4784px;left:195px;width:810px;display:flex;justify-content:space-around;font-size:11px;color:var(--ink)}
.footer-nav .active{color:var(--red)}
.footer-nav .sep{color:var(--muted)}
.copyright{position:absolute;top:4829px;left:0;width:1200px;text-align:center;font-size:11px;color:var(--ink)}
.footer-photo{left:0;top:4905px;width:1200px;height:312px;background:linear-gradient(180deg,rgba(200,212,222,0) 0%,#9aa3ab 35%,#6a6e72 70%,#4c4f52 100%)}
</style>
</head>
<body>

<!-- HERO -->
<section class="hero">
  <div class="hero-photo" role="img" aria-label="Mining processing plant with conveyor belts under a dusk sky"></div>
  <svg class="hero-curve" width="1200" height="700" viewBox="0 0 1200 700" aria-hidden="true">
    <path d="M0 588 Q600 790 1200 588 L1200 700 L0 700 Z" fill="#ffffff"/>
  </svg>
</section>

<nav class="nav">
  <span class="active">Home</span><span>About Us</span><span>Services ˅</span><span>Projects</span>
</nav>
<div class="brand"><span class="brand-dot"></span>Brevimor Inc.</div>
<span class="careers">Careers</span>
<a class="btn contact">Contact Us</a>
<div class="lang">
  <svg width="15" height="15" viewBox="0 0 16 16" aria-hidden="true"><circle cx="8" cy="8" r="6.5" fill="none" stroke="#141414" stroke-width="1.2"/><ellipse cx="8" cy="8" rx="3" ry="6.5" fill="none" stroke="#141414" stroke-width="1"/><line x1="1.5" y1="8" x2="14.5" y2="8" stroke="#141414" stroke-width="1"/></svg>
  ENG ˅
</div>

<p class="welcome">WELCOME TO <span>BREVIMOR</span></p>
<div class="welcome-dot"></div>
<h1 class="hero-title">WE'RE HERE TO PLAN &amp; SCHEDULE<br>YOUR <span class="accent">PROJECTS</span></h1>

<div class="circle-btn slide-prev"><svg width="12" height="12" viewBox="0 0 12 12"><path d="M8 2 L4 6 L8 10" fill="none" stroke="#fff" stroke-width="1.6"/></svg></div>
<div class="circle-btn slide-next"><svg width="12" height="12" viewBox="0 0 12 12"><path d="M4 2 L8 6 L4 10" fill="none" stroke="#141414" stroke-width="1.6"/></svg></div>
<div class="circle-btn scroll-down"><svg width="28" height="28" viewBox="0 0 28 28"><path d="M14 4 V23 M6 15 L14 23 L22 15" fill="none" stroke="#fff" stroke-width="2.4"/></svg></div>

<!-- WHO WE ARE -->
<div class="photo who-photo" role="img" aria-label="Excavator digging at sunset"></div>
<div class="who-faint">Brevimor</div>
<h2 class="who-title">WHO <span class="accent" style="color:var(--red)">WE</span> ARE</h2>
<p class="who-lead">It is a long established fact that a reader will be distracted by the readable content of a page when looking at its layout.</p>
<p class="who-text" style="top:955px">Lorem Ipsum is simply dummy text of the printing and typesetting industry. Lorem Ipsum has been the industry's standard dummy text ever since the 1500s, when an unknown printer took a galley of type and scrambled it to make a type specimen book. It has survived not only five centuries, but also the leap into electronic typesetting, remaining essentially unchanged.</p>
<p class="who-text" style="top:1055px">There are many variations of passages of Lorem Ipsum available, but the majority have suffered alteration in some form.</p>
<a class="btn who-btn">Learn More</a>
<div class="photo who-photo-2" role="img" aria-label="Aerial view of a stacker over an ore stockpile"></div>

<!-- SERVICES -->
<section class="services" role="img" aria-label="Construction cranes over a building site, tinted deep red"></section>
<h2 class="services-title">OUR SERVICES</h2>

<div class="svc" style="left:195px;top:1739px">
  <div class="svc-photo" role="img" aria-label="Molten metal pouring in a foundry" style="background:linear-gradient(160deg,#2a2220,#c8681f 50%,#3c2c26)"></div>
  <div class="svc-box">MINING AND<br>METALLURGY</div>
  <div class="svc-icon"></div>
  <div class="svc-arrow"><svg width="10" height="10" viewBox="0 0 10 10"><path d="M3 1 L7 5 L3 9" fill="none" stroke="#fff" stroke-width="1.6"/></svg></div>
</div>
<div class="svc" style="left:478px;top:1739px">
  <div class="svc-photo" role="img" aria-label="Highway traffic at sunset" style="background:linear-gradient(180deg,#f4c66a,#c9a07a 45%,#7a7c80)"></div>
  <div class="svc-box">INFRASTRUCTURE &amp;<br>TRANSPORTATION</div>
  <div class="svc-icon"></div>
  <div class="svc-arrow"><svg width="10" height="10" viewBox="0 0 10 10"><path d="M3 1 L7 5 L3 9" fill="none" stroke="#fff" stroke-width="1.6"/></svg></div>
</div>
<div class="svc" style="left:760px;top:1739px">
  <div class="svc-photo" role="img" aria-label="Tower crane against a pale sky" style="background:linear-gradient(160deg,#dfe6ee,#aeb8c4 55%,#6d7680)"></div>
  <div class="svc-box">CONSTRUCTION<br>MANAGEMENT</div>
  <div class="svc-icon"></div>
  <div class="svc-arrow"><svg width="10" height="10" viewBox="0 0 10 10"><path d="M3 1 L7 5 L3 9" fill="none" stroke="#fff" stroke-width="1.6"/></svg></div>
</div>
<div class="svc" style="left:195px;top:2136px">
  <div class="svc-photo" role="img" aria-label="Water treatment clarifier basins" style="background:linear-gradient(180deg,#8fb8d6,#2f9c8c 55%,#1f6e64)"></div>
  <div class="svc-box">WATER<br>TREATMENT</div>
  <div class="svc-icon"></div>
  <div class="svc-arrow"><svg width="10" height="10" viewBox="0 0 10 10"><path d="M3 1 L7 5 L3 9" fill="none" stroke="#fff" stroke-width="1.6"/></svg></div>
</div>
<div class="svc" style="left:478px;top:2136px">
  <div class="svc-photo" role="img" aria-label="Interior of a house under construction" style="background:linear-gradient(160deg,#e9d6b8,#f4ede2 50%,#c5a27a)"></div>
  <div class="svc-box">PROJECT<br>MANAGEMENT</div>
  <div class="svc-icon"></div>
  <div class="svc-arrow"><svg width="10" height="10" viewBox="0 0 10 10"><path d="M3 1 L7 5 L3 9" fill="none" stroke="#fff" stroke-width="1.6"/></svg></div>
</div>
<div class="svc" style="left:760px;top:2136px">
  <div class="svc-photo" role="img" aria-label="Construction plans, calculator and hard hat on a desk" style="background:linear-gradient(160deg,#e8e4de,#f1e3b0 60%,#cfc7bd)"></div>
  <div class="svc-box">CONSTRACT<br>MANAGEMENT</div>
  <div class="svc-icon"></div>
  <div class="svc-arrow"><svg width="10" height="10" viewBox="0 0 10 10"><path d="M3 1 L7 5 L3 9" fill="none" stroke="#fff" stroke-width="1.6"/></svg></div>
</div>

<!-- RECENT PROJECTS -->
<h2 class="projects-title">OUR RECENT <span class="accent">PROJECTS</span></h2>
<div class="proj" style="left:195px;top:2736px;width:437px;height:274px">
  <div class="photo" role="img" aria-label="Freight trucks, plane and city logistics montage" style="inset:0;background:linear-gradient(135deg,#3c5a86,#9aa6b8 45%,#c98a55 75%,#5a4b44)"></div>
  <span class="proj-label">INFRASTRUCTURE &amp; TRANSPORTATION</span>
</div>
<div class="proj" style="left:647px;top:2736px;width:358px;height:274px">
  <div class="photo" role="img" aria-label="Refinery lit at night" style="inset:0;background:linear-gradient(180deg,#0f2a52,#23508a 50%,#0c1a30)"></div>
  <span class="proj-label">ENERGY</span>
</div>
<div class="proj" style="left:195px;top:3022px;width:358px;height:272px">
  <div class="photo" role="img" aria-label="Bucket wheel excavator in an open-pit mine" style="background:linear-gradient(180deg,#4f7fc2,#9bb5d8 40%,#c47b45 70%,#6b4430);inset:0"></div>
  <span class="proj-label">MINING &amp; METALS</span>
</div>
<div class="proj" style="left:568px;top:3022px;width:437px;height:272px">
  <div class="photo" role="img" aria-label="Offshore oil platform at sea" style="inset:0;background:linear-gradient(180deg,#cfe1ef,#8fb0c8 50%,#2f4c66)"></div>
  <span class="proj-label">HYDROCARBONS</span>
</div>

<!-- BUILD BETTER -->
<section class="build" role="img" aria-label="Stockpile conveyor in the mine at night, tinted navy"></section>
<h2 class="build-title">BUILD A BETTER TOMORROW<br>WITH US</h2>
<p class="build-text">Lorem Ipsum is simply dummy text of the printing and typesetting industry. Lorem Ipsum has been the industry's standard dummy text ever since the 1500s.</p>
<a class="btn build-btn">FIND OUT MORE</a>

<!-- LATEST NEWS -->
<h2 class="news-title">LATEST <span class="accent">NEWS</span></h2>
<div class="circle-btn news-prev"><svg width="12" height="12" viewBox="0 0 12 12"><path d="M8 2 L4 6 L8 10" fill="none" stroke="#141414" stroke-width="1.6"/></svg></div>
<div class="circle-btn news-next"><svg width="12" height="12" viewBox="0 0 12 12"><path d="M4 2 L8 6 L4 10" fill="none" stroke="#fff" stroke-width="1.6"/></svg></div>

<article class="news-card" style="left:195px">
  <div class="photo news-photo" role="img" aria-label="Aerial view of layered mine terraces" style="background:linear-gradient(150deg,#6c8fb8,#d8a27a 45%,#e7c9b0 65%,#7e8ea4)"></div>
  <div class="news-body">
    <p class="news-date">JUN 23, 2023</p>
    <h3 class="news-head">There are many variations of pass-<br>ages of Lorem Ipsum</h3>
    <p class="news-text">It is a long established fact that a reader will be distracted by the readable content of a page when looking at its layout. The point of using Lorem Ipsum is that it has a more...</p>
    <a class="news-link">Learn More →</a>
  </div>
</article>
<article class="news-card" style="left:606px">
  <div class="photo news-photo" role="img" aria-label="Tower cranes over a building site at sunrise" style="background:linear-gradient(180deg,#f2d58a,#c8b28a 50%,#6d6456)"></div>
  <div class="news-body">
    <p class="news-date">JUN 23, 2023</p>
    <h3 class="news-head">There are many variations of pass-<br>ages of Lorem Ipsum</h3>
    <p class="news-text">It is a long established fact that a reader will be distracted by the readable content of a page when looking at its layout. The point of using Lorem Ipsum is that it has a more...</p>
    <a class="news-link">Learn More →</a>
  </div>
</article>

<!-- FOOTER -->
<footer class="footer"></footer>
<div class="footer-brand"><span class="brand-dot"></span>Brevimor Inc.</div>
<span class="social" style="left:509px" aria-label="Social profile 1"></span>
<span class="social" style="left:558px" aria-label="Social profile 2"></span>
<span class="social" style="left:606px" aria-label="Social profile 3"></span>
<span class="social" style="left:655px" aria-label="Social profile 4"></span>
<div class="footer-rule" style="top:4773px"></div>
<nav class="footer-nav">
  <span class="active">HOME</span><span class="sep">/</span><span>ABOUT US</span><span class="sep">/</span><span>SERVICES</span><span class="sep">/</span><span>PROJECTS</span><span class="sep">/</span><span>CAREERS</span>
</nav>
<div class="footer-rule" style="top:4810px"></div>
<p class="copyright">Copyright © 2023 Brevimor Inc. All Rights Reserved.</p>
<div class="photo footer-photo" role="img" aria-label="Two yellow mining haul trucks on a gravel quarry"></div>

</body>
</html>
```